Personal Development Model Graphic

I am creating a Personal Development/Coaching business and website and need some assistance with the development of a graphic that represents my methodology. I have already done what I consider to be a working version, but now it's time to have a professional design eye take a look at it and improve.

Specifically, I need assistance on color usage. I'd like each of the 8 areas of the model to have a color, and I've tried to utilize colors I feel are representative of the specific area(for example, purple for spirituality) but it doesn't really work for everything and perhaps additional thought could be put to that aspect of it.

Also, the model needs to work in reverse of the way it's pictured in the attached JPEG. So Friends needs to be first (top center)and then going clockwise, Spirituality needs to be in the 1:00 position not the 11:00 position and then continue around to Community, Family, Exercise, Career, Art/Creativity, and last at 11:00 Sexuality. I was going to update it before uploading, but I'm having trouble with Photoshop and just decided to pull the trigger on having a designer do it.

Thank you in advance for your creativity and ideas!

Industry/Entity Type

Business

Requirements
Nice to have
• It would be fantastic if it could feel modern, and high tech. I realize this is difficult with circles! But whatever you can do.

On color usage, it would again be wonderful to have colors that are more modern than traditional. I'll leave that to your discretion.

```html
<!DOCTYPE html>
<html lang="en">
<head>
<meta charset="UTF-8">
<title>Personal Development Model</title>
<link rel="stylesheet" href="https://fonts.googleapis.com/css2?family=Oswald:wght@500&display=swap">
<style>
  :root {
    --bg: #ffffff;
    --arrow: #bcbec0;
    --core: #ffdd15;
    --friends: #d81e5b;
    --spirituality: #6d6e71;
    --community: #7f3f98;
    --family: #8dc63f;
    --exercise: #12a89d;
    --career: #056839;
    --creativity: #f7941d;
    --sexuality: #be1e2d;
    --label: #ffffff;
  }
  html, body {
    margin: 0;
    padding: 0;
    width: 1200px;
    height: 900px;
    overflow: hidden;
    background: var(--bg);
  }
  .model {
    position: relative;
    width: 1200px;
    height: 900px;
    font-family: "Oswald", "Arial Narrow", sans-serif;
    font-weight: 500;
  }
  .model__arrows {
    position: absolute;
    inset: 0;
  }
  .model__arrow { fill: var(--arrow); }
  .node {
    position: absolute;
    display: flex;
    align-items: center;
    justify-content: center;
    text-align: center;
    border-radius: 50%;
    color: var(--label);
    text-transform: uppercase;
    line-height: 1.12;
    text-shadow: 1px 2px 2px rgba(0, 0, 0, 0.35);
    letter-spacing: -0.2px;
  }
  .node--area {
    width: 150px;
    height: 150px;
    margin: -75px 0 0 -75px;
    font-size: 27px;
  }
  .node--core {
    left: 600px;
    top: 450px;
    width: 222px;
    height: 222px;
    margin: -111px 0 0 -111px;
    background: var(--core);
    font-size: 46px;
  }
  .node--friends      { left: 600px; top: 206px; background: var(--friends); }
  .node--spirituality { left: 773px; top: 278px; background: var(--spirituality); font-size: 25px; }
  .node--community    { left: 844px; top: 450px; background: var(--community); font-size: 26px; }
  .node--family       { left: 773px; top: 622px; background: var(--family); }
  .node--exercise     { left: 600px; top: 694px; background: var(--exercise); }
  .node--career       { left: 428px; top: 622px; background: var(--career); }
  .node--creativity   { left: 356px; top: 450px; background: var(--creativity); }
  .node--sexuality    { left: 428px; top: 278px; background: var(--sexuality); }
</style>
</head>
<body>
  <main class="model" aria-label="Personal development model: eight life areas feeding into happiness">
    <svg class="model__arrows" width="1200" height="900" viewBox="0 0 1200 900" aria-hidden="true">
      <defs>
        <polygon id="inward-arrow" class="model__arrow"
          points="-12,-166 12,-166 12,-140 26,-140 0,-116 -26,-140 -12,-140"/>
      </defs>
      <g transform="translate(600 450)">
        <use href="#inward-arrow"/>
        <use href="#inward-arrow" transform="rotate(45)"/>
        <use href="#inward-arrow" transform="rotate(90)"/>
        <use href="#inward-arrow" transform="rotate(135)"/>
        <use href="#inward-arrow" transform="rotate(180)"/>
        <use href="#inward-arrow" transform="rotate(225)"/>
        <use href="#inward-arrow" transform="rotate(270)"/>
        <use href="#inward-arrow" transform="rotate(315)"/>
      </g>
    </svg>

    <div class="node node--area node--friends">Friends</div>
    <div class="node node--area node--spirituality">Spirituality</div>
    <div class="node node--area node--community">Community</div>
    <div class="node node--area node--family">Family</div>
    <div class="node node--area node--exercise">Exercise</div>
    <div class="node node--area node--career">Career</div>
    <div class="node node--area node--creativity">Art<br>Creativity</div>
    <div class="node node--area node--sexuality">Sexuality</div>

    <div class="node node--core">Happiness</div>
  </main>
</body>
</html>
```